Re-branding for Structural Engineering firm

We need new business cards as part of our current re-branding. We have a new logo (attached), so the card design should incorporate this color scheme. We are a structural engineering firm providing structural building design and seismic consulting services. The final design should communicate professionalism and stability, with a modern look and feel.

```html
<!DOCTYPE html>
<html lang="en">
<head>
<meta charset="utf-8">
<title>Northspan Engineering – Business Card</title>
<link href="https://fonts.googleapis.com/css2?family=Open+Sans:wght@400;600;700&display=swap" rel="stylesheet">
<style>
  :root {
    --brand-blue: #1f6fba;
    --brand-grey: #555a60;
    --card-white: #ffffff;
    --backdrop: #eef0f3;
    --text-muted: #4a4f55;
  }
  * { margin: 0; padding: 0; box-sizing: border-box; }
  html, body { width: 1200px; height: 800px; overflow: hidden; }
  body {
    background: var(--backdrop);
    font-family: "Open Sans", Verdana, sans-serif;
    position: relative;
  }
  .business-card {
    position: absolute;
    left: 75px; top: 100px;
    width: 1050px; height: 600px;
    background: var(--card-white);
    box-shadow: 0 12px 40px rgba(0,0,0,0.12);
    overflow: hidden;
  }
  .card-wave { position: absolute; inset: 0; width: 100%; height: 100%; }
  .brand {
    position: absolute;
    left: 36px; top: 62px;
    display: flex; align-items: center; gap: 22px;
  }
  .brand-square {
    width: 104px; height: 104px;
    background: var(--brand-blue);
  }
  .brand-name {
    font-weight: 700;
    font-size: 52px;
    line-height: 1.02;
    color: var(--brand-blue);
    letter-spacing: 0.5px;
  }
  .contact-list {
    position: absolute;
    left: 40px; top: 345px;
    list-style: none;
    color: var(--card-white);
    font-size: 24px;
    letter-spacing: 0.6px;
  }
  .contact-list li {
    display: flex; align-items: flex-start; gap: 18px;
    height: 45px;
  }
  .contact-list svg { width: 22px; height: 22px; flex: none; margin-top: 5px; }
  .contact-list .address { line-height: 1.2; font-size: 22px; }
  .person {
    position: absolute;
    right: 60px; top: 305px;
    text-align: center;
  }
  .person-name {
    font-weight: 700;
    font-size: 36px;
    color: var(--brand-blue);
  }
  .person-title {
    font-size: 22px;
    color: var(--text-muted);
    margin-top: -4px;
  }
</style>
</head>
<body>
  <main class="business-card">
    <svg class="card-wave" viewBox="0 0 1050 600" preserveAspectRatio="none" aria-hidden="true">
      <path d="M0,210 C240,200 480,250 660,330" fill="none" stroke="#1f6fba" stroke-width="6"/>
      <path d="M0,240 C320,240 520,420 760,495 C880,530 980,515 1050,470 L1050,600 L0,600 Z" fill="#1f6fba"/>
      <path d="M690,480 C820,520 960,500 1050,455" fill="none" stroke="#ffffff" stroke-width="5"/>
    </svg>

    <div class="brand">
      <div class="brand-square"></div>
      <div class="brand-name">NORTHSPAN<br>ENGINEERING</div>
    </div>

    <ul class="contact-list">
      <li>
        <svg viewBox="0 0 24 24" fill="#fff"><path d="M6.6 10.8a15 15 0 0 0 6.6 6.6l2.2-2.2c.3-.3.7-.4 1-.2 1.1.4 2.3.6 3.6.6.6 0 1 .4 1 1V20c0 .6-.4 1-1 1A17 17 0 0 1 3 4c0-.6.4-1 1-1h3.5c.6 0 1 .4 1 1 0 1.3.2 2.5.6 3.6.1.3 0 .7-.2 1z"/></svg>
        <span>555.201.4830</span>
      </li>
      <li>
        <svg viewBox="0 0 24 24" fill="none" stroke="#fff" stroke-width="2"><rect x="7" y="2" width="10" height="20" rx="2"/><line x1="11" y1="18" x2="13" y2="18"/></svg>
        <span>555.372.9146</span>
      </li>
      <li>
        <svg viewBox="0 0 24 24" fill="none" stroke="#fff" stroke-width="2"><rect x="3" y="6" width="18" height="12"/><path d="M3 6l9 7 9-7"/></svg>
        <span>dana@northspanse.com</span>
      </li>
      <li>
        <svg viewBox="0 0 24 24" fill="none" stroke="#fff" stroke-width="2"><circle cx="12" cy="12" r="9"/><path d="M3 12h18M12 3c3 3 3 15 0 18M12 3c-3 3-3 15 0 18"/></svg>
        <span>www.northspanse.com</span>
      </li>
      <li>
        <svg viewBox="0 0 24 24" fill="#fff"><path d="M12 2a7 7 0 0 0-7 7c0 5 7 13 7 13s7-8 7-13a7 7 0 0 0-7-7zm0 9.5A2.5 2.5 0 1 1 12 6.5a2.5 2.5 0 0 1 0 5z"/></svg>
        <span class="address">4410 Harbor Point Dr., Ste 210<br>Coralton, CA 92000</span>
      </li>
    </ul>

    <div class="person">
      <div class="person-name">Dana Morrow, S.E</div>
      <div class="person-title">Principal</div>
    </div>
  </main>
</body>
</html>
```